Market online tutoring + Back to School + give Support for students school work K to 12 Grade

To promote my tutoring business online need to create a two sided flyer. Need to get the attention of parents and educators who looking for help to support the digital learning of their students due to COVID-19 lock down. I need to project and differentiate that we offer support for online school with individualized learning . We tutor Elementary to High school students on all subjects you may take a look at my website qnacademyga.com for additional info and also I can provide
Updates

Hi All Due to Covid, we were unable to work on this project on time as originally planned. We were given an extension until March 15 and we will complete it by then. Sorry for any inconvenience and Thank you for your support. -QN Academy

Target Market(s)

Parents and students

Industry/Entity Type

Education

Requirements
Must have
• For online less fine print on the first page. The phone number and support text message. Back to School , Support Online learning KEV/NUR test prep should have some focus
Nice to have
• Discuss the platform We created a platform with live instructor interaction, virtual classroom, instructional videos, assessments, and practice to support every individual student’s need. We are confident in our ability to provide the most effective distance learning experience.
Should not have
• too much clunky and packed with content. Should be easy to read with color

```html
<!DOCTYPE html>
<html lang="en">
<head>
<meta charset="utf-8">
<title>QN Academy – Two-sided Flyer</title>
<link href="https://fonts.googleapis.com/css2?family=Montserrat:ital,wght@0,400;0,500;0,600;0,700;0,800;1,500;1,600&family=Open+Sans:wght@400;600;700&family=Oswald:wght@600&family=Kalam:wght@700&display=swap" rel="stylesheet">
<style>
:root{
  --navy:#0d3a4c;
  --red:#c3202f;
  --red-deep:#a81a27;
  --gray-text:#555a5e;
  --light-gray:#8d9092;
  --beige:#e6cfb0;
  --beige-dark:#d2b48e;
  --paper:#ffffff;
  --stage:#e4e5e6;
}
*{margin:0;padding:0;box-sizing:border-box}
html,body{width:1200px;height:906px;overflow:hidden}
body{background:var(--stage);position:relative;font-family:"Open Sans",sans-serif}
.flyer{position:absolute;top:104px;width:493px;height:697px;background:var(--paper);overflow:hidden}
.flyer--front{left:76px}
.flyer--back{left:630px;background:var(--navy)}
.abs{position:absolute}

/* FRONT */
.front-art{position:absolute;left:0;top:0;width:493px;height:320px}
.test-brands{left:28px;top:16px;font-family:"Montserrat",sans-serif;font-size:31px;line-height:1;letter-spacing:-1px}
.test-brands .light{color:var(--light-gray);font-weight:400}
.test-brands .bold{color:var(--navy);font-weight:800;font-style:italic}
.headline{font-family:"Montserrat",sans-serif;line-height:1}
.headline--big{color:var(--red);font-weight:800;font-size:53px;left:26px;top:56px;letter-spacing:-1px}
.headline--mid{color:var(--red);font-weight:800;font-size:44px;left:28px;top:141px;letter-spacing:-1px}
.headline--sub{color:var(--navy);font-weight:500;font-style:italic;font-size:27px}
.sub-1{left:27px;top:104px}
.sub-2{left:31px;top:181px}
.brand-name{right:22px;top:285px;display:flex;align-items:center;gap:7px;font-family:"Montserrat",sans-serif;font-weight:800;font-size:21px;color:var(--navy);background:var(--paper);padding:8px 12px;border-radius:4px;white-space:nowrap}
.brand-name .dot{width:14px;height:14px;border-radius:50%;background:var(--red)}
.platform-title{left:22px;top:300px;font-family:"Montserrat",sans-serif;font-weight:700;font-size:15px;color:var(--red)}
.feature{display:flex;align-items:center;gap:10px;font-family:"Montserrat",sans-serif;font-size:15.5px;line-height:1.1;color:var(--gray-text);white-space:nowrap}
.feature svg{flex:none;width:34px;height:34px;fill:var(--red)}
.confidence{left:34px;top:478px;width:420px;font-family:"Montserrat",sans-serif;font-size:15.5px;line-height:1.35;color:var(--gray-text)}
.front-base{left:0;top:500px;width:493px;height:197px}
.banner{left:23px;top:531px;width:450px;height:92px;background:var(--red);border-radius:5px;color:#fff;text-align:center;padding-top:5px;white-space:nowrap}
.banner__title{font-family:"Oswald",sans-serif;font-weight:600;font-size:28px;line-height:1.05;letter-spacing:.5px}
.banner__script{font-family:"Kalam",cursive;font-weight:700;font-size:19px;line-height:1.25}
.banner__note{font-family:"Montserrat",sans-serif;font-style:italic;font-weight:600;font-size:12px;line-height:1.2;margin-top:2px}
.contact{font-family:"Montserrat",sans-serif;color:#fff;text-align:center;line-height:1.1;white-space:nowrap}
.contact__label{font-size:19px;font-weight:500}
.contact__value{font-size:21px;font-weight:700}
.front-call{left:22px;top:636px;width:210px}
.front-visit{left:236px;top:639px;width:232px}

/* BACK */
.back-art{left:0;top:0;width:493px;height:215px}
.section-title{font-family:"Open Sans",sans-serif;font-weight:700;font-size:18px;color:#fff;left:24px}
.rule{left:24px;height:1px;background:rgba(255,255,255,.6)}
.why{display:flex;gap:8px;width:150px}
.why svg{flex:none;width:24px;height:24px;fill:#fff}
.why h3{font-family:"Open Sans",sans-serif;font-weight:700;font-size:10px;color:#fff;margin-bottom:3px;white-space:nowrap}
.why p{font-family:"Open Sans",sans-serif;font-size:8.3px;line-height:1.33;color:#fff;text-align:justify;width:99px}
.plan{width:127px;height:138px;background:#f2f2f2;border-radius:3px;text-align:center;font-family:"Open Sans",sans-serif}
.plan__head{height:31px;background:var(--red);color:#fff;font-weight:700;font-size:11px;line-height:31px;border-radius:3px 3px 0 0}
.plan__body{padding-top:11px;font-size:8.4px;line-height:14.8px;color:var(--gray-text)}
.plan__rate{color:var(--red);font-weight:700}
.plan__price{position:absolute;left:50%;bottom:-11px;transform:translateX(-50%);background:var(--red);color:#fff;font-family:"Open Sans",sans-serif;font-weight:700;font-size:17px;width:62px;height:27px;line-height:25px;border-radius:7px;border:2px solid var(--navy)}
.back-base{left:0;top:600px;width:493px;height:97px}
.cta{background:#fff;border-radius:4px;text-align:center;font-family:"Montserrat",sans-serif;color:var(--red);line-height:1.05;padding-top:9px;height:63px;top:614px;white-space:nowrap}
.cta__label{font-size:19px;font-weight:500}
.cta__value{font-size:21px;font-weight:700}
</style>
</head>
<body>

<!-- FRONT SIDE -->
<section class="flyer flyer--front">
  <svg class="front-art" viewBox="0 0 493 320" aria-hidden="true">
    <path d="M0 0H493V300C380 280 150 240 0 210Z" fill="var(--beige)"/>
    <path d="M0 212C150 245 340 280 493 302V310C340 292 150 258 0 232Z" fill="var(--navy)"/>
  </svg>
  <div class="abs" role="img" aria-label="Photo of two children in school backpacks lying on the floor as if flying" style="left:140px;top:0;width:353px;height:275px;background:radial-gradient(ellipse at 60% 55%,var(--beige-dark),var(--beige) 70%);clip-path:polygon(0 0,100% 0,100% 100%,0 88%)"></div>

  <div class="abs test-brands"><span class="light">KEV</span> <span class="bold">NUR</span></div>
  <div class="abs headline headline--big">LEARN</div>
  <div class="abs headline headline--sub sub-1">Any Where</div>
  <div class="abs headline headline--mid">LEARN</div>
  <div class="abs headline headline--sub sub-2">Online</div>

  <div class="abs brand-name"><span class="dot"></span>QN Academy</div>

  <div class="abs platform-title">We created a platform with</div>

  <div class="abs feature" style="left:32px;top:330px">
    <svg viewBox="0 0 34 34"><rect x="3" y="5" width="28" height="19" rx="2"/><rect x="0" y="25" width="34" height="4" rx="1"/><circle cx="17" cy="12" r="4" fill="#fff"/><path d="M10 22c1-5 13-5 14 0z" fill="#fff"/></svg>
    <span>Live instructor<br>Interaction</span>
  </div>
  <div class="abs feature" style="left:32px;top:380px">
    <svg viewBox="0 0 34 34"><path d="M2 6h13c1 0 2 1 2 2v22c0-1-1-2-2-2H2z"/><path d="M32 6H19c-1 0-2 1-2 2v22c0-1 1-2 2-2h13z"/><path d="M21 12l8 5-8 5z" fill="#fff"/></svg>
    <span>Virtual<br>Classroom</span>
  </div>
  <div class="abs feature" style="left:32px;top:425px">
    <svg viewBox="0 0 34 34"><rect x="2" y="3" width="22" height="26" rx="2"/><path d="M6 10h4M12 10h9M6 16h4M12 16h9M6 22h4" stroke="#fff" stroke-width="2"/><circle cx="25" cy="25" r="8" fill="#fff" stroke="var(--red)" stroke-width="2"/><path d="M23 21l6 4-6 4z"/></svg>
    <span>Instructional<br>Videos</span>
  </div>
  <div class="abs feature" style="left:214px;top:331px">
    <svg viewBox="0 0 34 34"><rect x="3" y="2" width="26" height="30" rx="2"/><path d="M7 9l2 2 3-4M7 17l2 2 3-4M7 25l2 2 3-4M15 9h10M15 17h10M15 25h10" stroke="#fff" stroke-width="2" fill="none"/></svg>
    <span>Assessments<br>&amp; Practice</span>
  </div>
  <div class="abs feature" style="left:214px;top:386px">
    <svg viewBox="0 0 34 34"><path d="M17 2l14 5-14 5-14-5z"/><circle cx="17" cy="15" r="6"/><path d="M4 34c0-9 6-13 13-13s13 4 13 13z"/></svg>
    <span>Support every<br>Individual Student’s need.</span>
  </div>

  <p class="abs confidence">We are confident in our ability to provide&nbsp; the most effective distance learning experience.</p>

  <svg class="abs front-base" viewBox="0 0 493 197" aria-hidden="true">
    <path d="M0 52C120 80 330 98 493 100V197H0Z" fill="var(--navy)"/>
  </svg>

  <div class="abs banner">
    <div class="banner__title">CONTINUE LEARNING FROM HOME</div>
    <div class="banner__script">Digital learning during COVID-19 lockdown.</div>
    <div class="banner__note">We tutor Elementary to High school students on all subjects</div>
  </div>

  <div class="abs contact front-call"><div class="contact__label">Call us</div><div class="contact__value">404-555-0142</div></div>
  <div class="abs contact front-visit"><div class="contact__label">Visit us</div><div class="contact__value">qnacademyga.com</div></div>
</section>

<!-- BACK SIDE -->
<section class="flyer flyer--back">
  <div class="abs" role="img" aria-label="Photo of two young children using laptops in a bright classroom" style="left:0;top:0;width:493px;height:215px;background:linear-gradient(180deg,#efe9e2,#d9cfc3)"></div>
  <svg class="abs back-art" viewBox="0 0 493 215" aria-hidden="true">
    <path d="M0 170C150 155 330 165 493 205V215H0Z" fill="var(--navy)"/>
    <path d="M0 172C160 150 340 168 470 203C330 172 160 160 0 178Z" fill="var(--red)"/>
  </svg>

  <h2 class="abs section-title" style="top:188px">Why us</h2>
  <div class="abs rule" style="top:212px;width:445px"></div>

  <div class="abs why" style="left:24px;top:224px">
    <svg viewBox="0 0 24 24"><path d="M12 3a9 9 0 00-9 9v6h5v-7H5a7 7 0 0114 0h-3v7h5v-6a9 9 0 00-9-9z"/></svg>
    <div><h3>Support</h3><p>Lorem ipsum dolor sit amet, consectetur adipi-scing elit, sed do eiusmod tempor incididunt ut labore et dolore magna aliqua.</p></div>
  </div>
  <div class="abs why" style="left:168px;top:224px">
    <svg viewBox="0 0 24 24"><rect x="2" y="2" width="16" height="20" rx="1"/><circle cx="10" cy="9" r="3" fill="var(--navy)"/><circle cx="18" cy="18" r="5"/><path d="M15.5 18l2 2 3-3.5" stroke="var(--navy)" stroke-width="1.6" fill="none"/></svg>
    <div><h3>Effective Curriculum</h3><p>Lorem ipsum dolor sit amet, consectetur adipi-scing elit, sed do eiusmod tempor incididunt ut labore et dolore magna aliqua.</p></div>
  </div>
  <div class="abs why" style="left:313px;top:224px">
    <svg viewBox="0 0 24 24"><rect x="9" y="2" width="14" height="11" fill="none" stroke="#fff" stroke-width="1.6"/><circle cx="5" cy="5" r="2.5"/><path d="M3 9h5l4 2-1 1-3-1v11H6v-6H5v6H3z"/></svg>
    <div><h3>Awesome Teachers</h3><p>Lorem ipsum dolor sit amet, consectetur adipi-scing elit, sed do eiusmod tempor incididunt ut labore et dolore magna aliqua.</p></div>
  </div>
  <div class="abs why" style="left:24px;top:319px">
    <svg viewBox="0 0 24 24"><path d="M7 10V7a5 5 0 0110 0" fill="none" stroke="#fff" stroke-width="2"/><rect x="4" y="10" width="16" height="12" rx="1"/><rect x="11" y="14" width="2" height="4" fill="var(--navy)"/></svg>
    <div><h3>Unlimited access</h3><p>Lorem ipsum dolor sit amet, consectetur adipi-scing elit, sed do eiusmod tempor incididunt ut labore et dolore magna aliqua.</p></div>
  </div>
  <div class="abs why" style="left:168px;top:319px">
    <svg viewBox="0 0 24 24"><path d="M2 11V3h8l12 12-8 8z"/><circle cx="6.5" cy="7" r="1.8" fill="var(--navy)"/></svg>
    <div><h3>Easy Pricing</h3><p>Lorem ipsum dolor sit amet, consectetur adipi-scing elit, sed do eiusmod tempor incididunt ut labore et dolore magna aliqua.</p></div>
  </div>
  <div class="abs why" style="left:313px;top:320px">
    <svg viewBox="0 0 24 24"><rect x="1" y="1" width="22" height="14" rx="1"/><path d="M5 4h6v8H5zM13 4h6v8h-6z" fill="var(--navy)"/><path d="M4 20c2-3 5-3 8 0s6 3 8 0" stroke="#fff" stroke-width="2" fill="none"/></svg>
    <div><h3>Unlimited Online practice</h3><p>Lorem ipsum dolor sit amet, consectetur adipi-scing elit, sed do eiusmod tempor incididunt ut labore et dolore magna aliqua.</p></div>
  </div>

  <h2 class="abs section-title" style="top:413px">Available Courses</h2>
  <div class="abs rule" style="top:439px;width:433px"></div>

  <div class="abs plan" style="left:26px;top:451px">
    <div class="plan__head">Starter</div>
    <div class="plan__body"><span class="plan__rate">Monthly Plan&nbsp; $100</span><br>Unlimited Course Access<br>Unlimited online Practice<br>24x7 support<br>Certification</div>
    <div class="plan__price">$100</div>
  </div>
  <div class="abs plan" style="left:185px;top:451px">
    <div class="plan__head">Medium</div>
    <div class="plan__body"><span class="plan__rate">Monthly Plan&nbsp; $200</span><br>Unlimited Course Access<br>Unlimited online Practice<br>24x7 support<br>Certification</div>
    <div class="plan__price">$200</div>
  </div>
  <div class="abs plan" style="left:335px;top:451px">
    <div class="plan__head">Premium</div>
    <div class="plan__body"><span class="plan__rate">Monthly Plan&nbsp; $300</span><br>Unlimited Course Access<br>Unlimited online Practice<br>24x7 support<br>Certification</div>
    <div class="plan__price">$300</div>
  </div>

  <svg class="abs back-base" viewBox="0 0 493 97" aria-hidden="true">
    <path d="M0 38C150 45 350 40 493 22V97H0Z" fill="var(--red)"/>
  </svg>
  <div class="abs cta" style="left:29px;width:196px"><div class="cta__label">Call us</div><div class="cta__value">404-555-0142</div></div>
  <div class="abs cta" style="left:243px;width:218px"><div class="cta__label">Visit us</div><div class="cta__value">qnacademyga.com</div></div>
</section>

</body>
</html>
```